Web Design Project: Executive Coach

PLEASE check out http://tarvell.com.sg/x/PixelGuild/PixelGuild_Brief/Blank.html

It is a better description of what I am after. It includes everything in this brief and in an easier format. (And...I don't have your design skills, so it doesn't look great.)

========

What the site offers
-
I am about to launch a one-person company that provides three services:
1) executive coaching
2) leadership training
3) psychotherapy to adults

My Unique Selling Point
-
My unique selling point is that I am a coach who is also a relatively senior psychologist. However, psychologists can be seen as scary and that may put people off.

The Biggest Challenge: The Target Audience
-
One challenge is that because I sell 3 services, I want to appeal to more than one demographic. They are:

1) The representative from HR of a company who wants to buy a leadership course or find a coach for an executive in the company. (Usually mid-40’s and older.)

2) The executives who will take the selection made by the head of HR and may choose me from 3 or 4 other options. (Usually late 30’s to mid 40’s. Both men and women. From multinational companies.)

3) Psychotherapy clients who are coming to be directly, not via HR, and who don’t want to feel insecure that they aren’t executives but still may be a good fit to work with me. (More women than men. Age 34-45. Typically have some European or American exposure.)

The Problem
-
The executives I see may or may not have some psychological concerns, but most will quite like that I am a psychologist as long as I’m not “scary” but “kind”. (Kind is key.) So while it is important to show I am a therapist, I don't want it to make executives embarrassed when a colleague says “Oh, I looked at this guy’s website. You aren't in therapy are you?”

As mentioned above, please check out the following link: http://tarvell.com.sg/x/PixelGuild/PixelGuild_Brief/Blank.html

________
Please note, I originally posted this as 584207 Executive Coaching, Leadership Training, and Psychotherapy Website. With the help of one designer and also PixelGuild customer support, I realized that I had requested only the design of a website, not the coding. I had offered the maximum amount, US$1000 (refundable). I am resubmitting the project here and I have guaranteed the funds. I am lowering the payment as I am now aware that I was only asking for design. I apologize for any inconvenience. And thank your for being interested in this project.
Updates

Reason: I would love to get started on the coding next week. So I hope to get your proposals in the next 3 days.

Target Market(s)

Primary audience: 34-44 year old men and women with some European / North American exposure

Industry/Entity Type

Leadership

Requirements
Must have
• Video on home page
Nice to have
• I would like have quotes slide in to a couple of the pages. These may have a photo of the author attached.

I would like WorkLoop integration with my business's WorkLoop page. (I haven't made one yet, so I'm not sure how it works.)

```html
<!DOCTYPE html>
<html lang="en">
<head>
<meta charset="utf-8">
<title>Tarvell Consulting</title>
<link href="https://fonts.googleapis.com/css2?family=Gelasio:ital@0;1&family=Roboto+Condensed:wght@300;400&family=Arimo&display=swap" rel="stylesheet">
<style>
:root{
  --bg:#ffffff;
  --brand:#7d8ba1;
  --heading:#6c7b91;
  --nav:#4f5966;
  --body:#5d5d5d;
  --author:#5b78a4;
  --rule:#e6e8eb;
  --footer:#8c97a6;
  --social-top:#5d9bd6;
  --social-bot:#2f6fb3;
}
*{margin:0;padding:0;box-sizing:border-box}
html,body{width:854px;height:1200px;overflow:hidden;background:var(--bg)}
.page{position:relative;width:1080px;height:1518px;transform:scale(0.7907);transform-origin:0 0}
.abs{position:absolute}
.brand{left:0;width:1068px;top:16px;text-align:center}
.brand-name{font-family:"Roboto Condensed",sans-serif;font-weight:300;font-size:34px;line-height:38px;color:var(--brand)}
.brand-tag{font-family:"Roboto Condensed",sans-serif;font-weight:300;font-size:14px;color:var(--brand);margin-top:4px}
.nav{left:141px;width:785px;top:101px;display:flex;justify-content:space-between;font-family:Gelasio,serif;font-size:14px;color:var(--nav)}
.quote{left:0;width:1068px;top:144px;text-align:center;font-family:Gelasio,serif;font-style:italic;font-size:21px;line-height:30px;color:var(--heading)}
.quote-by{left:770px;top:196px;font-family:Gelasio,serif;font-size:13.5px;color:#7a808a}
.rule{left:160px;width:750px;height:1px;background:linear-gradient(90deg,transparent,var(--rule) 15%,var(--rule) 85%,transparent)}
.h2{font-family:"Roboto Condensed",sans-serif;font-weight:300;font-size:19.5px;color:var(--heading);text-align:center}
.card{background:#fff;border:1px solid #e2e2e2;box-shadow:0 1px 4px rgba(0,0,0,.15);overflow:hidden}
.card-text{position:absolute;left:8px;right:12px;top:12px;font-family:Arimo,sans-serif;font-size:11.5px;line-height:14px;color:#606060}
.card-photo{position:absolute;left:0;right:0;bottom:0}
.sub{font-family:Arimo,sans-serif;font-size:11px;color:#777;text-align:center}
.video-frame{left:348px;top:725px;width:372px;height:313px;background:#fff;border:1px solid #ddd;box-shadow:0 1px 4px rgba(0,0,0,.18)}
.quote-col{font-family:Gelasio,serif;font-size:12.3px;line-height:16px;color:var(--body);width:252px}
.author{font-family:"Roboto Condensed",sans-serif;font-size:12.5px;line-height:14.5px;color:var(--author);text-align:right;width:252px}
.social{left:467px;width:133px;height:34px;border-radius:3px;background:linear-gradient(var(--social-top),var(--social-bot));border:1px solid #2a5f9a;display:flex;align-items:center;font-family:"Roboto Condensed",sans-serif;font-size:13px;color:#fff}
.social .sq{width:22px;height:22px;background:#fff;opacity:.9;margin:0 14px 0 8px;border-radius:2px}
.foot-links{left:0;width:1068px;display:flex;justify-content:center;gap:10px;font-family:"Roboto Condensed",sans-serif;font-size:12.5px;color:var(--footer)}
.copy{color:#4e5e78}
</style>
</head>
<body>
<div class="page">
  <header class="abs brand">
    <div class="brand-name">Tarvell Consulting</div>
    <div class="brand-tag">Transforming teams, leaders, and individuals</div>
  </header>

  <nav class="abs nav">
    <span>Home</span><span>Coaching</span><span>Leadership Training</span><span>Psychotherapy</span><span>Clients</span><span>Testimonials</span><span>Contact</span><span>About Dr. Tarvell</span>
  </nav>

  <div class="abs quote">“You’re off to great places, today is your day!<br>Your mountain is waiting, so… get on your way!”</div>
  <div class="abs quote-by">Dr. Wendle</div>
  <div class="abs rule" style="top:232px"></div>

  <h2 class="abs h2" style="left:141px;width:250px;top:302px">Leadership Training</h2>
  <div class="abs card" style="left:141px;top:333px;width:251px;height:268px">
    <p class="card-text">Creating custom-made leadership workshops to fit the needs of organizations</p>
    <div class="card-photo" role="img" aria-label="Photo of a smiling business team with a leader in front" style="top:52px;background:linear-gradient(90deg,#e9e3de,#cdb9ab 45%,#3b3737 75%,#e8e5e2)"></div>
  </div>

  <h2 class="abs h2" style="left:408px;width:250px;top:269px">Executive Training</h2>
  <div class="abs card" style="left:408px;top:299px;width:251px;height:268px">
    <p class="card-text">Partnering with clients one-on-one to actualize their professional potential.</p>
    <div class="card-photo" role="img" aria-label="Photo of two business people shaking hands" style="top:52px;background:linear-gradient(90deg,#f4f4f4,#2e3440 20%,#3a3f48 45%,#eceae8 60%,#2d2f35 80%,#f4f4f4)"></div>
  </div>

  <h2 class="abs h2" style="left:675px;width:250px;top:302px">Psychotherapy</h2>
  <div class="abs card" style="left:675px;top:333px;width:251px;height:268px">
    <p class="card-text">Deepening personal insight and developing behaviors to grow in well-being.</p>
    <div class="card-photo" role="img" aria-label="Photo of an open hand holding a small tree by the sea" style="top:52px;background:linear-gradient(#f1f4f6,#dfe6ea 55%,#c9c8bf 75%,#9fb98a)"></div>
  </div>

  <div class="abs rule" style="top:658px"></div>

  <h2 class="abs h2" style="left:0;width:1068px;top:675px">David Tarvell, My Father</h2>
  <p class="abs sub" style="left:0;width:1068px;top:700px">A little talk about my beloved father.</p>

  <div class="abs video-frame"></div>
  <div class="abs" style="left:357px;top:733px;width:354px;height:296px;background:#111"></div>
  <div class="abs" role="img" aria-label="Video still of a man speaking at a lectern" style="left:357px;top:767px;width:354px;height:203px;background:linear-gradient(90deg,#9e8f6a,#b9a981 40%,#a79774 70%,#8c8371)"></div>
  <svg class="abs" style="left:357px;top:733px" width="354" height="296" viewBox="0 0 354 296">
    <circle cx="346" cy="13" r="6" fill="#ddd"/><rect x="345" y="11" width="2" height="6" fill="#111"/><rect x="345" y="8" width="2" height="2" fill="#111"/>
    <rect x="145" y="114" width="62" height="42" rx="9" fill="#1b1b1b" opacity=".85"/>
    <path d="M170 126 L186 135 L170 144 Z" fill="#fff"/>
    <rect x="0" y="265" width="354" height="6" fill="#d11c1c"/>
    <circle cx="7" cy="268" r="5" fill="#ddd"/>
    <rect x="0" y="271" width="354" height="25" fill="#222"/>
    <path d="M18 278 L28 284 L18 290 Z" fill="#aaa"/>
    <path d="M50 281 h4 l5 -4 v14 l-5 -4 h-4 z" fill="#aaa"/>
    <text x="76" y="288" font-family="Arimo,sans-serif" font-size="9" fill="#eee">0:00</text>
    <circle cx="273" cy="284" r="4" fill="#888"/>
    <text x="290" y="288" font-family="Arimo,sans-serif" font-size="9" fill="#999">Streamly</text>
    <path d="M334 278 h-4 v4 M340 278 h4 v4 M334 291 h-4 v-4 M340 291 h4 v-4" stroke="#aaa" fill="none" stroke-width="1.5"/>
  </svg>

  <div class="abs rule" style="top:1062px"></div>

  <h2 class="abs h2" style="left:0;width:1068px;top:1079px">Testimonials</h2>

  <p class="abs quote-col" style="left:141px;top:1134px">I have been very impressed with Adrian’s energy, intelligence and relational IQ.&nbsp; He combines a practical view focused on results with a deeper understanding of&nbsp; the emotional issues that can impact those results.&nbsp; He is a joy to work with and has helped a number of our executives significantly improve their performance.</p>
  <p class="abs author" style="left:140px;top:1276px">Rob Kessing, Chief Executive Officer,<br>Brightwell Food Corporation (2013)</p>

  <p class="abs quote-col" style="left:408px;top:1134px">An effective executive coach, Adrian combines world-class academic preparation with a wide base of&nbsp; experience and a natural charisma that easily wins the trust and respect of&nbsp; his clients.</p>
  <p class="abs author" style="left:407px;top:1228px">Mark Oliver Delane, Vice President -<br>Corporate Human Resources,<br>Brightwell Food Corporation (2013)</p>

  <p class="abs quote-col" style="left:675px;top:1134px">Your course on leadership was truly transformational as the insight that you gave on leadership cannot be gathered in totality from the books alone. Your teaching methods are so inspiring and motivating that no student of&nbsp; yours can forget the essence of your teaching.</p>
  <p class="abs author" style="left:674px;top:1262px">Ravi Sethan, Additional Director General of Police/<br>Police Commissioner, Bangalore, India (2012)</p>

  <div class="abs rule" style="top:1340px"></div>

  <div class="abs social" style="top:1353px" aria-label="Follow on Chatterly"><span class="sq"></span>FOLLOW ME</div>
  <div class="abs social" style="top:1392px" aria-label="Follow on WorkLoop"><span class="sq"></span>FOLLOW ME</div>

  <p class="abs foot-links" style="top:1442px"><span>Home</span><span>Coaching</span><span>Leadership Training</span><span>Psychotherapy</span></p>
  <p class="abs foot-links" style="top:1460px"><span>Clients</span><span>Testimonials</span><span>Contact</span><span>About Dr. Tarvell</span></p>
  <p class="abs foot-links copy" style="top:1478px"><span>Copyright © 2013 Adrian Tarvell</span></p>
</div>
</body>
</html>
```